Redesign Of Hotel Coupon/Voucher 8.5 x 11

I would like to redesign my voucher.

Please provide me a color flyer design but one that would be easy on printing costs...for example printing from home computer/printer.

I would like to see some color designs...maybe some black and white and also full graphics and even basic like the plum tally voucher I provided as a sample. The 2 night hotel stay is the voucher I need to redesign...

Target Market(s)

Consumers

Industry/Entity Type

Hotel

Requirements
Must have
• exact text in current designs---look official, credible and trust worthy
Nice to have
• I would like to redesign my voucher.
• Please provide me a color flyer design but one that would be easy on printing costs...for example printing from home computer/printer.
• I would like to see some color designs...maybe some black and white and also full graphics and even basic like the plum tally voucher I provided as a sample. The 2 night hotel stay is the voucher I need to redesign...
Should not have

```html
<!DOCTYPE html>
<html lang="en">
<head>
<meta charset="utf-8">
<title>2 Night Hotel Stay Certificate</title>
<link rel="stylesheet" href="https://fonts.googleapis.com/css2?family=Montserrat:wght@400;500;600;700&family=Open+Sans:wght@400;600;700;800&family=Merriweather+Sans:wght@800&display=swap">
<style>
:root{
  --page-bg:#d9d4cc;
  --paper:#ffffff;
  --panel-gray:#e6e7ea;
  --brand-blue:#1f3c96;
  --brand-navy:#141f5c;
  --heading-blue:#2a3c9e;
  --ink:#1b1b1f;
  --line:#4a4a4a;
  --accent-red:#e02b2b;
}
*{box-sizing:border-box;margin:0;padding:0}
html,body{width:1200px;height:1000px;overflow:hidden;background:var(--page-bg)}
.flyer{position:absolute;left:226px;top:20px;width:748px;height:960px;background:var(--paper);overflow:hidden;font-family:"Open Sans",sans-serif;color:var(--ink);box-shadow:0 2px 6px rgba(0,0,0,.15)}
.hero{position:absolute;left:0;top:0;width:748px;height:279px;background:linear-gradient(180deg,#9aa3ad 0%,#c9b89a 38%,#8a6d4f 70%,#3d3a39 100%)}
.hero-fade{position:absolute;left:0;bottom:0;width:100%;height:40px;background:linear-gradient(180deg,rgba(255,255,255,0),#fff)}
.hero-title{position:absolute;left:0;top:226px;width:748px;text-align:center;padding-left:80px;font-family:"Merriweather Sans",sans-serif;font-weight:800;font-size:41px;color:#fff;text-shadow:2px 3px 4px rgba(0,0,0,.8);letter-spacing:.5px}
.compliments{position:absolute;left:533px;top:0;width:202px;height:207px;background:#fff;text-align:center;font-family:"Montserrat",sans-serif;color:var(--heading-blue);font-weight:700}
.compliments h2{font-size:14.5px;line-height:17px;margin-top:31px}
.compliments p{font-size:11.5px;line-height:20px}
.compliments .contact{margin-top:33px}
.destinations{position:absolute;left:28px;top:287px;width:691px;height:85px;background:var(--panel-gray);padding:2px 8px;font-size:9.1px;line-height:13.3px;font-weight:600}
.terms-tab{position:absolute;left:0;top:376px;width:200px;height:24px;background:var(--brand-blue);clip-path:polygon(0 0,100% 0,93% 100%,0 100%);color:#fff;font-family:"Montserrat",sans-serif;font-weight:600;font-size:12.5px;line-height:24px;padding-left:34px}
.terms-rule{position:absolute;left:0;top:398px;width:30px;height:3px;background:var(--brand-blue)}
.terms{position:absolute;left:28px;top:412px;width:691px;height:219px;background:var(--panel-gray);padding:3px 4px;font-size:8.1px;line-height:11px;text-align:justify;overflow:hidden}
.form-area{position:absolute;left:0;top:638px;width:748px;height:322px;background:var(--panel-gray)}
.form-col{position:absolute;font-family:"Montserrat",sans-serif}
.form-col h3{font-size:12.5px;font-weight:600;color:var(--ink);margin-bottom:6px}
.field{display:flex;align-items:flex-end;font-size:10px;font-weight:600;height:16.7px}
.field .label{white-space:nowrap}
.field .blank{flex:1;border-bottom:1px solid var(--line);margin-left:6px;height:10px}
.billing{left:34px;top:10px;width:215px}
.billing .label{width:50px}
.shipping-head{margin-top:12px}
.redeem{position:absolute;left:258px;top:0;width:232px;height:322px}
.redeem svg{position:absolute;left:0;top:0}
.redeem-body{position:absolute;left:18px;top:36px;width:196px;color:#fff;font-family:"Montserrat",sans-serif}
.redeem-intro{text-align:center;font-size:10px;line-height:12.4px}
.redeem h4{font-size:11.5px;font-weight:600;margin-top:17px}
.redeem .step{font-size:8.4px;font-weight:600;margin-top:7px}
.redeem .link{text-align:center;font-size:8.4px;text-decoration:underline;margin-top:6px}
.redeem .address{text-align:center;font-size:8px;line-height:9.6px;margin-top:6px}
.redeem .cert{font-size:11.5px;font-weight:600;margin-top:14px;line-height:16px}
.redeem .cert span{margin-left:20px}
.redeem .expiry{color:var(--accent-red);margin-left:4px}
.payment{left:500px;top:10px;width:225px}
.payment .method{font-size:10px;font-weight:600;margin-bottom:10px}
.checks{display:grid;grid-template-columns:64px 1fr;row-gap:6px;padding-left:22px;font-size:10.5px;font-weight:500;margin-bottom:8px}
.checks label{display:flex;align-items:center;gap:4px}
.box{width:13px;height:13px;border:1px solid var(--line);background:#fff}
.payment .field .blank{margin-left:4px}
.agree{font-size:10.5px;font-weight:600;margin-top:14px}
.notes{font-family:"Open Sans",sans-serif;font-size:6.9px;line-height:8.5px;margin-top:12px}
.notes p{margin-bottom:5px}
.code{position:absolute;right:24px;bottom:18px;font-size:6.5px;font-weight:700;font-family:"Open Sans",sans-serif}
</style>
</head>
<body>
<main class="flyer">
  <div class="hero" role="img" aria-label="Photo of a hotel room window table with coffee cups and juice overlooking city skyscrapers"><div class="hero-fade"></div></div>
  <h1 class="hero-title">2 Night Hotel Stay</h1>
  <section class="compliments">
    <h2>THE CERTIFICATE IS<br>COMPLIMENTS OF:</h2>
    <div class="contact"><p>NAME</p><p>PHONE NUMBER</p><p>E-MAIL ADDRESS</p></div>
  </section>

  <section class="destinations">Destinations Available: Anaheim, CA--Atlanta, GA--Atlantic City, NJ--Branson, MO--Cancun, MX--Charleston, SC--Coeur d' Alene, ID--Daytona Beach, FL--Destin, FL--Ft. Lauderdale, FL--Ft. Meyers, FL--Gatlinburg, TN--Hilton Head, SC--Honolulu, HI--Kissimmee, FL--Lake Tahoe, CA--Las Vegas, NV--Myrtle Beach, SC--Niagara Falls/Buffalo Area, NY--Orlando, FL--Ormond Beach, FL--Palm Springs, CA--Pigeon Forge, TN--St. Petersburg, FL--San Antonio, TX--San Diego, CA--San Francisco, CA--Sedona, AZ--Sonoma Wine Country, CA--St. George, UT--Tampa, FL--Williamsburg, VA--Wisconsin Dells, WI--Tallahassee, FL--Augusta, GA--Columbia, SC--New York, NY--Florence, SC--Washington, D.C.--Chicago, IL--Salt Lake City, UT--Hollywood, CA-Dayton, OH--Tucson, AZ--Niagra Falls, ON/CAN--Seattle, WA--Portland, OR--Antioch, CA--San Mateo, CA--Brunswick, GA--Nashville, TN</section>

  <div class="terms-tab">TERMS &amp; CONDITIONS</div>
  <div class="terms-rule"></div>
  <section class="terms">This certificate will be considered void if bartered or purchased for legal tender by the recipient. This certificate is valid for a reservation request form offering 2adults 21 years of age and older plus up to 2 children under the age of 18, 2 nights of hotel accommodations in the city of their choice of available cities. The costto activate this certificate to receive the reservation request form is just a one-time non-refundable $14.95 processing fee. The cost upon requesting reservationsis just a tax &amp; fee deposit of $33 per night. Taxes &amp; fees usually range from $12-$33 per night depending on when and where you travel to. If the taxes &amp; feesare less than the $33 per night the difference will be refunded after travel is completed. 30 days advance reservation notice is required. In order to guaranteethat you will show up to your booked reservation you will be required to pay a REFUNDABLE $50 "Reservation Guarantee Deposit". If you send in your traveldates, etc and you do not end up traveling then the reservation guarantee deposit will not be refundable. 7 days before and after holidays and conventions arenot available. This offer is valid 7 days a week subject to availability. Friday and Saturday nights will require a surcharge of $20 per night. A $5 per person pernight surcharge is enforced for each child up to 2 children under the age of 18. This offer is not valid for group travel. The recipient of this certificate isresponsible for all expenses including but not limited to: transfers, food, gratuities, all pertinent fees, taxes, hotel surcharges, resort fees and any othermiscellaneous expenses. If you activate this certificate online you will be able to instantly print your reservation request form. If you cannot print your ownreservation request form we will mail it to you. You should receive it in the mail within 14 days. This certificate cannot be combined with any other promotionalvacation offer. The expiration date on this certificate pertains only to activation of this certificate and not actual travel. You must activate this certificate by theexpiration date printed on this certificate in order to receive the reservation request form. You must fill out the reservation request form with your destinationchoices and arrival dates and mail it to our fulfillment department within 6 months after activation, however travel can be completed within 12 months afteractivation. You will be required to give the travel agency multiple arrival dates and destinations. Only one 2 Night Hotel certificate Per Household Per Year. Thiscertificate has no cash surrender value, void if discontinued and where prohibited by law. The terms of this offer are subject to change without notice. Do not relyupon representations other than what is printed on this certificate or the reservation request form. CST # 0000000</section>

  <section class="form-area">
    <div class="form-col billing">
      <h3>BILLING INFORMATION</h3>
      <div class="field"><span class="label">Name:</span><span class="blank"></span></div>
      <div class="field"><span class="label">Address:</span><span class="blank"></span></div>
      <div class="field"><span class="label">City:</span><span class="blank"></span></div>
      <div class="field"><span class="label">State:</span><span class="blank"></span></div>
      <div class="field"><span class="label">Zip Code:</span><span class="blank"></span></div>
      <div class="field"><span class="label">Country:</span><span class="blank"></span></div>
      <div class="field"><span class="label">Phone:</span><span class="blank"></span></div>
      <div class="field"><span class="label">Email:</span><span class="blank"></span></div>
      <h3 class="shipping-head">SHIPPING INFORMATION</h3>
      <div class="field"><span class="label">Name:</span><span class="blank"></span></div>
      <div class="field"><span class="label">Address:</span><span class="blank"></span></div>
      <div class="field"><span class="label">City:</span><span class="blank"></span></div>
      <div class="field"><span class="label">State:</span><span class="blank"></span></div>
      <div class="field"><span class="label">Zip Code:</span><span class="blank"></span></div>
      <div class="field"><span class="label">Country:</span><span class="blank"></span></div>
    </div>

    <div class="redeem">
      <svg width="232" height="322" viewBox="0 0 232 322" aria-hidden="true">
        <rect x="0" y="0" width="232" height="322" fill="var(--brand-navy)"/>
        <rect x="18" y="28" width="196" height="294" fill="var(--brand-blue)"/>
        <polygon points="0,0 18,0 18,28" fill="var(--panel-gray)"/>
        <polygon points="232,0 214,0 214,28" fill="var(--panel-gray)"/>
        <polygon points="18,0 214,0 214,28 18,28" fill="var(--brand-navy)"/>
      </svg>
      <div class="redeem-body">
        <p class="redeem-intro">Simply fill out the form on thiscer-tificate and enclose payment of U.S.$14.95. Northpay, Crestcard, Orbex, Lumen Card, Debit Card, CheckCard, Check &amp; Money Orders are allaccepted.</p>
        <h4>3 WAYS TO REDEEM:</h4>
        <p class="step">1. For expedited redemption go to:</p>
        <p class="link">www.StayPerksClub.com</p>
        <p class="step">2. Fax* certificate to: 1-800-555-0147</p>
        <p class="step">3. Mail* to:</p>
        <p class="address">Redemption Center<br>4210 Harbor View Rd Ste B #120<br>Bay Ridge, Ca 90000</p>
        <p class="cert">CERTIFICATE ID:<span>-10002</span><br>EXPIRATION DATE:<span class="expiry">04/08/2017</span></p>
      </div>
    </div>

    <div class="form-col payment">
      <h3>PAYMENT INFORMATION</h3>
      <p class="method">Payment Method:</p>
      <div class="checks">
        <label><span class="box"></span>Check</label><label><span class="box"></span>Money Order</label>
        <label><span class="box"></span>Northpay</label><label><span class="box"></span>Crestcard</label>
        <label><span class="box"></span>Orbex</label><label><span class="box"></span>Lumen Card</label>
      </div>
      <div class="field"><span class="label">Name On Card:</span><span class="blank"></span></div>
      <div class="field"><span class="label">Card # (16 digits):</span><span class="blank"></span></div>
      <div class="field"><span class="label">Expiration Date:</span><span class="blank" style="flex:0 0 24px"></span><span style="margin:0 6px">/</span><span class="blank" style="flex:0 0 68px;margin-left:0"></span></div>
      <div class="field"><span class="label">CV2#**:</span><span class="blank" style="flex:0 0 52px;margin-left:10px"></span></div>
      <p class="agree">I agree to terms and conditions</p>
      <div class="field"><span class="label">Signature:</span><span class="blank"></span></div>
      <div class="notes">
        <p>"Redemption Center" will appear on your billing statement.</p>
        <p>Make checks and money orders payable to:<br>"Redemption Center"<br>* You will receive your information by mail within 10 days.</p>
        <p>** Last 3 digits on back of card (4 digits on front of Orbex).</p>
      </div>
    </div>
    <span class="code">2NIL -10002</span>
  </section>
</main>
</body>
</html>
```